Kestrow-Holdings. Limestone; improving the world

New Limestone company and need logo design.
Limestone offsets carbon mitigation industries restore and replenish soil fertilities in the Prairies, the breadbasket of the world. At the same time, Limestone is proving a critical emergent component of carbon capture sequestration technology will therefore play a critical role in the development of the western Canadian energy industries
Our limestone resources are situated in the foothills of the Canadian Rockies well-positioned above the sprawling fields of the vast peace district.
Target Market(s)
Agriculture and oli sites
Logo Text
Kestrow Holdings
Number of Pages Required
3 page

```html
<!DOCTYPE html>
<html lang="en">
<head>
<meta charset="utf-8">
<title>Kestrow Holdings</title>
<link href="https://fonts.googleapis.com/css2?family=Gentium+Book+Plus:wght@400;700&family=Mulish:wght@400;500&display=swap" rel="stylesheet">
<style>
  :root {
    --brown: #35281f;
    --ink: #2b2420;
    --text: #3a3430;
    --green: #5db53f;
    --btn-green: #7cc84f;
    --white: #ffffff;
    --panel: rgba(248, 246, 244, 0.9);
    --rule: #5a4c42;
  }
  * { margin: 0; padding: 0; box-sizing: border-box; }
  html, body { width: 740px; height: 1200px; overflow: hidden; background: var(--white); }
  body { position: relative; font-family: "Gentium Book Plus", "Palatino Linotype", serif; color: var(--text); }

  .site-header { position: absolute; left: 0; top: 0; width: 740px; height: 55px; background: var(--white); }
  .brand { position: absolute; left: 61px; top: 8px; }
  .brand-name { font-size: 17.5px; color: var(--ink); line-height: 1; display: flex; align-items: center; gap: 7px; }
  .brand-mark { width: 12px; height: 12px; background: var(--ink); display: inline-block; }
  .brand-tagline { font-size: 11px; color: var(--green); margin-top: 4px; text-align: right; line-height: 1; }
  .main-nav { position: absolute; top: 26px; left: 0; width: 740px; font-size: 9.6px; color: var(--ink); }
  .main-nav a { position: absolute; color: inherit; text-decoration: none; white-space: nowrap; }
  .main-nav .is-active { font-weight: 700; }

  .hero { position: absolute; left: 0; top: 55px; width: 740px; height: 317px;
    background: linear-gradient(160deg, #c98f6c 0%, #d7a488 35%, #b77a58 70%, #a66f50 100%); }
  .hero-card { position: absolute; left: 404px; top: 67px; width: 253px; height: 164px;
    background: var(--panel); border-right: 3px solid var(--green); padding: 20px 6px 0 10px; text-align: right; }
  .hero-title { font-family: "Mulish", sans-serif; font-weight: 500; font-size: 13.6px; line-height: 22px; color: var(--ink); }
  .hero-btn { display: inline-block; margin-top: 7px; background: var(--brown); color: var(--btn-green);
    font-family: "Mulish", sans-serif; font-size: 12.5px; padding: 3px 5px 4px; text-decoration: none; }

  .mission { position: absolute; left: 62px; top: 412px; width: 320px; font-size: 19px; line-height: 27px; color: var(--ink); }

  .info { position: absolute; left: 411px; width: 270px; }
  .info h2 { font-weight: 400; font-size: 16.5px; color: var(--ink); line-height: 1.2; margin-bottom: 7px; }
  .info p { font-size: 10.2px; line-height: 17px; }
  .info-about { top: 413px; }
  .info-special { top: 539px; }

  .feature { position: absolute; left: 61px; top: 676px; width: 618px; height: 268px;
    background: radial-gradient(ellipse at 75% 55%, #9fd44a 0%, #4f9a24 40%, #2f7a18 70%, #1d5a10 100%),
                linear-gradient(90deg, #d9e79a, #6ba82c); }
  .feature-card { position: absolute; left: 12px; top: 51px; width: 253px; height: 165px;
    background: var(--panel); border-left: 3px solid var(--green); padding: 24px 12px 0 8px; }
  .feature-card h2 { font-weight: 400; font-size: 17px; color: var(--ink); margin-bottom: 6px; line-height: 1.1; }
  .feature-card p { font-size: 10.2px; line-height: 17px; }

  .site-footer { position: absolute; left: 0; top: 1026px; width: 740px; height: 174px; background: var(--brown); color: var(--white); }
  .footer-company { position: absolute; left: 62px; top: 16px; font-size: 11.3px; font-weight: 700; }
  .footer-address { position: absolute; left: 62px; top: 39px; font-size: 10.2px; line-height: 15px; }
  .footer-contact { position: absolute; left: 62px; top: 101px; font-size: 10.2px; line-height: 15px; }
  .footer-rule { position: absolute; left: 61px; top: 141px; width: 620px; height: 1px; background: var(--rule); }
  .footer-copy { position: absolute; left: 0; top: 151px; width: 740px; text-align: center; font-size: 9.4px; }
</style>
</head>
<body>
  <header class="site-header">
    <div class="brand">
      <div class="brand-name"><span class="brand-mark"></span>Kestrow Holdings</div>
      <div class="brand-tagline">Improving The World</div>
    </div>
    <nav class="main-nav">
      <a class="is-active" style="left:440px">Home</a>
      <a style="left:500px">About Us</a>
      <a style="left:573px">FAQs</a>
      <a style="left:631px">Contact Us</a>
    </nav>
  </header>

  <section class="hero" role="img" aria-label="Photo of young corn plants growing in reddish farm soil">
    <div class="hero-card">
      <p class="hero-title">Limestone Offsets Carbon Mitigation Industries Restore And Replenish Soil Fertilities In The Prairies, The Breadbasket of The World.</p>
      <a class="hero-btn">Contact Us Today</a>
    </div>
  </section>

  <p class="mission">Our Mission&nbsp; Is to Improve our world by responsibly meeting society’s needs for quality lime and limestone products.</p>

  <section class="info info-about">
    <h2>About Us</h2>
    <p>Lorem ipsum dolor sit amet, consectetuer adpiscing elit, sed diam nonummy nibh euismod tincidunt ut laoreet dolore magna aliquam erat volutpat. Ut wisi enim ad minim veniam, quis nostrud exerci tatiofdn ullamcorper suscipit lobortis nisl ut aliquip commodo.</p>
  </section>

  <section class="info info-special">
    <h2>Special Opportunities</h2>
    <p>Our limestone resources are situated in the foothills of the Canadian Rockies well-positioned above the sprawling fields of the vast peace district.</p>
  </section>

  <section class="feature" role="img" aria-label="Photo of an open hand holding a glowing green leafy light bulb against blurred foliage, with eco icons around it">
    <div class="feature-card">
      <h2>Sustainability</h2>
      <p>Lorem ipsum dolor sit amet, contetr adpiscing elit, sed diam nonummy nibh eumod tincidunt ut laoreet dolore magna aliquam erat volutpat. Ut wisi enim ad minim veniam, quis nostrud exerci tatiofdn ullamcorper.</p>
    </div>
  </section>

  <footer class="site-footer">
    <div class="footer-company">Kestrow-Holdings Management, LLC</div>
    <div class="footer-address">88 Harlow Ave, 9th Floor<br>Calder, NY 10412</div>
    <div class="footer-contact">For any inquiries, please contact<br>mara@<br>.com</div>
    <div class="footer-rule"></div>
    <div class="footer-copy">Copyright © 2021 Kestrow-Holdings.&nbsp; All Right Reserved.</div>
  </footer>
</body>
</html>
```